Cork Meadow Excursions Post Card/Flyer

Postcard/flyer needs to convey our mission: to provide an authentic, boutique wine tour of exceptional quality with first class customer service. It needs to be clean and high quality. Less is more :) Worthy of 5 star hotel concierges handing them to a guest. I provided an old flyer my friend made and my competitors flyer. Please use these just as reference, but i want to see your creativity. I like the format of "Gentle Harvest" -scan 91-flyer BUT I don't want to copy.

Target Market(s)

Couples, travelers, hotel employees, local industry, etc...

Industry/Entity Type

Boutique

Requirements
Must have
• Must have bullet points of the my previous reference flyer and any photos .Please use website for reference too.
• Yelp, trip advisor affirmations Plus Instagram
• "Group and Private Tours available"
• "Mention this card for 10% off any tour" - low key please
• corkmeadowexcursions.com, info@corkmeadowexcursions.com, 805-219-6384
Nice to have
• clean lines , simple and elegant
• double sided please
Should not have
• Not too busy.

```html
<!DOCTYPE html>
<html lang="en">
<head>
<meta charset="utf-8">
<title>Cork Meadow Excursions – Rack Card</title>
<link href="https://fonts.googleapis.com/css2?family=Tinos&family=Source+Sans+3:wght@400;600&display=swap" rel="stylesheet">
<style>
  :root {
    --forest: #1f6341;
    --forest-deep: #185535;
    --ink: #4a4a4a;
    --swoosh: #c9cacc;
    --paper: #ffffff;
    --backdrop: #ecebe8;
    --gold: #b08a4e;
    --serif: "Tinos", "Times New Roman", serif;
    --sans: "Source Sans 3", "Helvetica Neue", Arial, sans-serif;
  }
  * { box-sizing: border-box; margin: 0; padding: 0; }
  html, body {
    width: 1194px; height: 1200px; overflow: hidden;
    background: var(--backdrop);
  }
  .card {
    position: absolute; top: 110px;
    width: 467px; height: 980px;
    background: var(--paper);
    box-shadow: 0 4px 14px rgba(0,0,0,.18);
    overflow: hidden;
  }
  .card--front { left: 97px; }
  .card--back { left: 630px; }
  .card__art { position: absolute; inset: 0; }

  .brand {
    position: absolute; top: 48px; left: 0; right: 0;
    display: flex; flex-direction: column; align-items: center; gap: 18px;
  }
  .brand__dot {
    width: 46px; height: 46px; border-radius: 50%;
    background: var(--forest);
  }
  .brand__name {
    font-family: var(--serif); font-size: 23px; letter-spacing: 2px;
    color: var(--forest); text-transform: uppercase;
  }

  .headline {
    position: absolute; left: 0; right: 0; text-align: center;
    font-family: var(--serif); font-size: 27px; line-height: 36px;
  }
  .tagline {
    position: absolute; left: 0; right: 0; text-align: center;
    font-family: var(--sans); font-size: 16.5px;
  }
  .card--front .headline { top: 758px; color: var(--paper); }
  .card--front .tagline { top: 840px; color: var(--paper); }
  .card--back .headline { top: 378px; color: var(--forest); }
  .card--back .tagline { top: 462px; color: var(--ink); }

  .divider {
    position: absolute; top: 513px; left: 119px; width: 240px; height: 2px;
    background: linear-gradient(90deg, transparent, var(--gold) 20%, var(--gold) 80%, transparent);
  }

  .features {
    position: absolute; top: 538px; left: 40px; list-style: none;
    font-family: var(--sans); font-size: 16.5px; color: var(--ink);
  }
  .features li {
    display: flex; align-items: center; gap: 14px; height: 44px;
  }
  .features svg { flex: none; }

  .offer {
    position: absolute; top: 716px; left: 0; right: 0; text-align: center;
    font-family: var(--serif); font-size: 15px; color: var(--forest);
  }

  .socials {
    position: absolute; top: 816px; left: 0; right: 0;
    display: flex; justify-content: center; gap: 21px;
  }
  .socials span {
    width: 30px; height: 30px; border-radius: 50%;
    border: 1.5px solid rgba(255,255,255,.85);
  }
  .tours-note {
    position: absolute; top: 866px; left: 0; right: 0; text-align: center;
    font-family: var(--sans); font-size: 15.5px; letter-spacing: .8px;
    color: var(--paper); text-transform: uppercase;
  }

  .phone-band {
    position: absolute; top: 905px; left: 0; right: 0; height: 30px;
    display: flex; align-items: center; justify-content: center; gap: 7px;
    background: var(--paper);
    font-family: var(--sans); font-weight: 600; font-size: 16px; color: #333;
  }
  .web-band {
    position: absolute; top: 935px; left: 0; right: 0; bottom: 0;
    display: flex; align-items: center; justify-content: center;
    background: var(--forest);
    font-family: var(--sans); font-size: 16.5px; letter-spacing: .6px; color: var(--paper);
  }
</style>
</head>
<body>

<section class="card card--front">
  <svg class="card__art" width="467" height="980" viewBox="0 0 467 980">
    <defs>
      <linearGradient id="vineyardTones" x1="0" y1="0" x2="0" y2="1">
        <stop offset="0" stop-color="#e9c98f"/>
        <stop offset=".35" stop-color="#b98a4e"/>
        <stop offset=".6" stop-color="#6f7a2c"/>
        <stop offset="1" stop-color="#3f5a1c"/>
      </linearGradient>
    </defs>
    <path d="M0,300 C120,215 300,190 467,192 L467,212 C300,210 130,236 0,318 Z" fill="var(--swoosh)"/>
    <path d="M0,332 C130,246 300,222 467,222 L467,622 C380,692 200,722 0,707 Z" fill="url(#vineyardTones)" role="img" aria-label="Sunlit rows of vines across rolling hills at golden hour"/>
    <path d="M0,714 C200,730 380,702 467,632 L467,652 C380,724 200,758 0,742 Z" fill="var(--swoosh)"/>
    <path d="M0,750 C200,764 380,730 467,660 L467,905 L0,905 Z" fill="var(--forest)"/>
  </svg>

  <div class="brand">
    <span class="brand__dot"></span>
    <span class="brand__name">Cork Meadow Excursions</span>
  </div>

  <h1 class="headline">Come Explore Santa Barbara<br>Wine Country with us!</h1>
  <p class="tagline">An authentic and boutique wine tour experience</p>

  <div class="phone-band">
    <svg width="18" height="18" viewBox="0 0 18 18"><circle cx="9" cy="9" r="8" fill="none" stroke="#333" stroke-width="1.5"/><path d="M6.2,4.8 L7.6,6.6 L6.9,7.6 C7.5,8.9 8.6,10.1 10,10.8 L11,10.1 L12.9,11.5 L12.1,12.9 C8.6,12.6 5.3,9.3 5,5.7 Z" fill="#333"/></svg>
    805 219 6384
  </div>
  <div class="web-band">www.corkmeadowexcursions.com</div>
</section>

<section class="card card--back">
  <svg class="card__art" width="467" height="980" viewBox="0 0 467 980">
    <defs>
      <linearGradient id="guestsTones" x1="0" y1="0" x2="0" y2="1">
        <stop offset="0" stop-color="#9fa48a"/><stop offset="1" stop-color="#6e5a4a"/>
      </linearGradient>
      <linearGradient id="grapesTones" x1="0" y1="0" x2="0" y2="1">
        <stop offset="0" stop-color="#5f7a2e"/><stop offset="1" stop-color="#3d3a4a"/>
      </linearGradient>
      <linearGradient id="picnicTones" x1="0" y1="0" x2="0" y2="1">
        <stop offset="0" stop-color="#8fa9c2"/><stop offset=".5" stop-color="#7f8a5a"/><stop offset="1" stop-color="#9a9486"/>
      </linearGradient>
    </defs>
    <rect x="0" y="177" width="118" height="164" fill="url(#guestsTones)" role="img" aria-label="Couple enjoying a glass of wine on a vineyard patio"/>
    <rect x="120" y="177" width="228" height="164" fill="url(#grapesTones)" role="img" aria-label="Dark grape clusters hanging among green vine leaves"/>
    <rect x="350" y="177" width="117" height="164" fill="url(#picnicTones)" role="img" aria-label="Guide serving guests at an outdoor picnic table"/>
    <path d="M0,842 C120,782 300,756 467,756 L467,768 C300,770 120,798 0,858 Z" fill="var(--swoosh)"/>
    <path d="M0,866 C120,806 300,776 467,774 L467,905 L0,905 Z" fill="var(--forest)"/>
  </svg>

  <div class="brand">
    <span class="brand__dot"></span>
    <span class="brand__name">Cork Meadow Excursions</span>
  </div>

  <h2 class="headline">Come Explore Santa Barbara<br>Wine Country with us!</h2>
  <p class="tagline">An authentic and boutique wine tour experience</p>
  <div class="divider"></div>

  <ul class="features">
    <li><svg width="18" height="18" viewBox="0 0 18 18"><circle cx="9" cy="9" r="7.5" fill="none" stroke="var(--forest)" stroke-width="1.5"/><path d="M7.5,5.5 L11,9 L7.5,12.5" fill="none" stroke="var(--forest)" stroke-width="1.8"/></svg>Premium wine tasting at boutique wineries</li>
    <li><svg width="18" height="18" viewBox="0 0 18 18"><circle cx="9" cy="9" r="7.5" fill="none" stroke="var(--forest)" stroke-width="1.5"/><path d="M7.5,5.5 L11,9 L7.5,12.5" fill="none" stroke="var(--forest)" stroke-width="1.8"/></svg>Safe and comfortable luxury vehicles</li>
    <li><svg width="18" height="18" viewBox="0 0 18 18"><circle cx="9" cy="9" r="7.5" fill="none" stroke="var(--forest)" stroke-width="1.5"/><path d="M7.5,5.5 L11,9 L7.5,12.5" fill="none" stroke="var(--forest)" stroke-width="1.8"/></svg>Picnic lunch in vineyard setting</li>
    <li><svg width="18" height="18" viewBox="0 0 18 18"><circle cx="9" cy="9" r="7.5" fill="none" stroke="var(--forest)" stroke-width="1.5"/><path d="M7.5,5.5 L11,9 L7.5,12.5" fill="none" stroke="var(--forest)" stroke-width="1.8"/></svg>Local expert guides</li>
  </ul>

  <p class="offer">Mention this card for 10% off any tour</p>

  <div class="socials" aria-label="Social profiles">
    <span></span><span></span><span></span><span></span><span></span>
  </div>
  <p class="tours-note">Group and private tours available</p>

  <div class="phone-band">
    <svg width="18" height="18" viewBox="0 0 18 18"><circle cx="9" cy="9" r="8" fill="none" stroke="#333" stroke-width="1.5"/><path d="M6.2,4.8 L7.6,6.6 L6.9,7.6 C7.5,8.9 8.6,10.1 10,10.8 L11,10.1 L12.9,11.5 L12.1,12.9 C8.6,12.6 5.3,9.3 5,5.7 Z" fill="#333"/></svg>
    805 219 6384
  </div>
  <div class="web-band">www.corkmeadowexcursions.com</div>
</section>

</body>
</html>
```